Creative Magazine Ad - fusing comfort, culture and cuisine for a food supply company

Hello and welcome to this project!

We need an ad for our company, Kela Supply Co, that is going to be in a magazine read by the Australian Army based in Papua New Guinea.

We want an ad that makes people stop and look. The key message is that even though Papua New Guinea is exotic, the food can be the same (as in Australia). And we want to show off what our company does – supplying great food that caters for all.

Your design should include:

Size:
• 1 page at 15cm height x 19.6cm width
Pictures:
• Our logo – Kela Supply Co – where people can see it
• Pictures or elements that capture the tropical landscape, tribal culture and or essence of Papua New Guinea mixed with pictures of Australian food like barbeque, steaks, pies, roast vegetables etc.
Text to add:
• Title: "Taste of Home in the Tropics: Your Australian Culinary Guide in Papua New Guinea”
• Message: "Our mission is to manufacture and procure a diverse range of high-quality food products, catering to the unique needs of defence camps, and supplying small to large wholesalers, retailers, restaurants, hotels, and caterers throughout Papua New Guinea. We are dedicated to supporting our defence forces with the comforts of home, while serving the broader community with exceptional culinary offerings."
• And our contact details:
+675 314 2691
www.ksv.com.pg
sales@kelasupplyco.com.pg

What we need:
• A graphic for printing for the magazine.
• A digital version to use online.

Thanks again – any questions please ask :)

A Bit About Us
Kela Supply Co Ltd is a 100% PNG-owned and managed business and is proud to be one of the largest food supply companies in the country. Our ability to supply a wide range of premium imported, local and in-house manufactured products from our Butchery and Bakery has contributed to the rock-solid reputation for quality and services that Kela Supply now enjoys throughout PNG.

We are proud to also sell our wide range of products through our retail outlets (Tova Grill Haus, Tova Crust Haus and Lute Grill Haus) and our popular Quick Service Restaurants (Reef Stacker and Orb Tart Nook). Our Catering division (Tova Welo Catering) owns a vast array of commercial catering equipment and has experience catering for large-scale events in PNG. We are the only company in Papua New Guinea that has the technology to provide “tamper proof” cold and hot individual meal solutions that can be delivered in temperature-controlled vehicles to locations in Port Moresby but also as a solution to large-scale mining camp catering needs.

```html
<!DOCTYPE html>
<html lang="en">
<head>
<meta charset="utf-8">
<title>Kela Supply Co – Taste of Home in the Tropics</title>
<link rel="stylesheet" href="https://fonts.googleapis.com/css2?family=Oswald:wght@600;700&family=Poppins:wght@400;600&family=Roboto+Condensed:ital,wght@1,700&display=swap">
<style>
  :root {
    --backdrop: #383838;
    --paper: #ffffff;
    --paper-shade: #eef0f2;
    --ink: #1b1b1b;
    --brand-red: #e31e25;
    --text: #262626;
  }
  html, body { margin: 0; padding: 0; width: 1200px; height: 1200px; overflow: hidden; background: var(--backdrop); }
  .ad {
    position: absolute; left: 57px; top: 180px; width: 1086px; height: 839px;
    background: linear-gradient(120deg, var(--paper) 0%, var(--paper) 45%, var(--paper-shade) 100%);
    overflow: hidden;
    box-shadow: 0 6px 18px rgba(0,0,0,.45);
  }
  .artwork { position: absolute; inset: 0; }
  .brand { position: absolute; left: 35px; top: 34px; width: 220px; height: 112px; }
  .brand-badge { position: absolute; left: 150px; top: 0; width: 64px; height: 25px; border-radius: 4px; background: var(--brand-red); }
  .brand-mark { position: absolute; left: 0; top: 38px; width: 62px; height: 62px; border-radius: 50%; background: var(--brand-red); }
  .brand-name {
    position: absolute; left: 74px; top: 34px; margin: 0;
    font: 700 33px/35px 'Oswald', sans-serif; color: var(--ink);
  }
  .brand-name span { display: block; white-space: nowrap; }
  .tagline {
    position: absolute; left: 47px; top: 166px; margin: 0;
    font: italic 700 15px/1 'Roboto Condensed', sans-serif; color: var(--ink); white-space: nowrap;
  }
  .headline { position: absolute; left: 33px; top: 210px; margin: 0; font-family: 'Oswald', sans-serif; font-weight: 700; }
  .headline span { display: block; white-space: nowrap; font-size: 82px; line-height: 87px; }
  .headline .line-dark { color: var(--ink); }
  .headline .line-red { color: var(--brand-red); }
  .subhead { position: absolute; left: 34px; top: 398px; margin: 0; font-family: 'Oswald', sans-serif; font-weight: 600; }
  .subhead span { display: block; white-space: nowrap; font-size: 38px; line-height: 46px; }
  .subhead .sub-dark { color: var(--ink); }
  .subhead .sub-red { color: var(--brand-red); }
  .mission {
    position: absolute; left: 35px; top: 513px; width: 372px; margin: 0;
    font: 400 16.4px/24.7px 'Poppins', sans-serif; color: var(--text);
  }
  .contacts { position: absolute; left: 35px; top: 774px; display: flex; }
  .contact { display: flex; align-items: center; gap: 9px; font: 600 18px/1 'Poppins', sans-serif; color: var(--brand-red); white-space: nowrap; }
  .contact.phone { width: 190px; }
  .contact.web { width: 214px; }
  .contact-icon { width: 27px; height: 27px; flex: none; }
</style>
</head>
<body>
<main class="ad">
  <svg class="artwork" width="1086" height="839" viewBox="0 0 1086 839">
    <defs>
      <linearGradient id="festival" x1="0" y1="0" x2="0" y2="1">
        <stop offset="0" stop-color="#3d86c9"/>
        <stop offset="0.3" stop-color="#7a8a6a"/>
        <stop offset="0.55" stop-color="#b2402e"/>
        <stop offset="0.8" stop-color="#5a3a24"/>
        <stop offset="1" stop-color="#2f5d2e"/>
      </linearGradient>
      <radialGradient id="steak" cx="0.5" cy="0.5" r="0.6">
        <stop offset="0" stop-color="#6b3b2a"/>
        <stop offset="0.7" stop-color="#8a4a30"/>
        <stop offset="1" stop-color="#c94a32"/>
      </radialGradient>
      <radialGradient id="pies" cx="0.5" cy="0.5" r="0.6">
        <stop offset="0" stop-color="#e2a95a"/>
        <stop offset="0.7" stop-color="#c98b4a"/>
        <stop offset="1" stop-color="#9a6a48"/>
      </radialGradient>
    </defs>
    <path d="M455 0 H492 C520 220 600 470 760 620 C880 730 990 760 1086 760 V839 H1060 C940 839 820 790 720 700 C560 560 470 300 455 0 Z" fill="var(--brand-red)"/>
    <path role="img" aria-label="Papua New Guinea highland festival performer in feathered headdress and shell necklaces against a blue sky" d="M490 0 H1086 V745 C990 745 880 712 770 610 C610 460 525 220 490 0 Z" fill="url(#festival)"/>
    <circle role="img" aria-label="Grilled steak slices on roasted vegetables with fresh herbs" cx="617" cy="578" r="161" fill="url(#steak)" stroke="var(--brand-red)" stroke-width="8"/>
    <circle role="img" aria-label="Three golden baked meat pies on a cooling rack" cx="878" cy="711" r="118" fill="url(#pies)" stroke="var(--brand-red)" stroke-width="8"/>
  </svg>

  <div class="brand">
    <div class="brand-badge"></div>
    <div class="brand-mark"></div>
    <p class="brand-name"><span>Kela Supply</span><span>Co Ltd</span></p>
  </div>
  <p class="tagline">“100% PNG Owned &amp; Operated”</p>

  <h1 class="headline">
    <span class="line-dark">Taste of Home</span>
    <span class="line-red">in the Tropics:</span>
  </h1>
  <h2 class="subhead">
    <span class="sub-dark">Your Australian Culinary Guide</span>
    <span class="sub-red">in Papua New Guinea</span>
  </h2>

  <p class="mission">Our mission is to manufacture and procure a diverse range of high-quality food products, catering to the unique needs of defence camps, and supplying small to large wholesalers, retailers, restaurants, hotels, and caterers throughout Papua New Guinea. We are dedicated to supporting our defence forces with the comforts of home, while serving the broader community with exceptional culinary offerings.</p>

  <div class="contacts">
    <div class="contact phone">
      <svg class="contact-icon" viewBox="0 0 28 28"><circle cx="14" cy="14" r="14" fill="var(--ink)"/><path d="M10 8 l3 3 -1.6 1.8 c.8 1.8 2 3 3.8 3.8 L17 15 l3 3 -1.8 2 c-4.5-.4-9.8-5.7-10.2-10.2 Z" fill="#fff"/></svg>
      <span>+675 314 2691</span>
    </div>
    <div class="contact web">
      <svg class="contact-icon" viewBox="0 0 28 28"><circle cx="14" cy="14" r="14" fill="var(--ink)"/><g fill="none" stroke="#fff" stroke-width="1.3"><circle cx="14" cy="14" r="7"/><ellipse cx="14" cy="14" rx="3" ry="7"/><path d="M7 14 H21 M8.5 10.5 H19.5 M8.5 17.5 H19.5"/></g></svg>
      <span>www.ksv.com.pg</span>
    </div>
    <div class="contact email">
      <svg class="contact-icon" viewBox="0 0 28 28"><circle cx="14" cy="14" r="14" fill="var(--ink)"/><g fill="none" stroke="#fff" stroke-width="1.4"><rect x="7.5" y="9.5" width="13" height="9" rx="1"/><path d="M7.5 10 L14 15 L20.5 10"/></g></svg>
      <span>sales@kelasupplyco.com.pg</span>
    </div>
  </div>
</main>
</body>
</html>
```